Tamkor, a service provider dedicated to improving the performance of a website

Tamkor offers optimization and performance improvement for all types of websites (showcase sites, e-commerce, ...), with the aim of improving their ranking on Vintrel and their customer transformation rate. The main benefits consist in optimizing the factors of a site. In addition, we also offer content creation (description of product sheets, services, ...), Vintrel Ads campaign management, migration version for Prestashop / Wordpress, etc. The design must be a fresh image, dynamic, why not "fun", but also serious. No favorite color, carte blanche on this point;)

```html
<!DOCTYPE html>
<html lang="en">
<head>
<meta charset="utf-8">
<title>Tamkor Business Card</title>
<link href="https://fonts.googleapis.com/css2?family=Lato:ital,wght@0,400;0,700;0,900;1,400;1,700&display=swap" rel="stylesheet">
<style>
  :root {
    --canvas: #cccccc;
    --brand-blue: #3a4f9b;
    --brand-deep: #1f3f86;
    --card-white: #ffffff;
    --ink-white: #ffffff;
  }
  * { box-sizing: border-box; margin: 0; padding: 0; }
  html, body {
    width: 1200px; height: 675px; overflow: hidden;
    background: var(--canvas);
    font-family: "Lato", sans-serif;
  }
  .stage {
    width: 1200px; height: 675px;
    display: flex; align-items: center; justify-content: center; gap: 40px;
  }
  .card {
    position: relative;
    width: 540px; height: 309px;
    border-radius: 16px;
    overflow: hidden;
  }
  .card-back {
    background: var(--brand-blue);
    display: flex; align-items: center; justify-content: center;
  }
  .wordmark {
    font-family: "Lato", sans-serif;
    font-weight: 900;
    letter-spacing: -1px;
    line-height: 1;
  }
  .card-back .wordmark { color: var(--ink-white); font-size: 84px; }
  .card-front { background: var(--card-white); }
  .front-wave { position: absolute; inset: 0; }
  .card-front .wordmark {
    position: absolute; left: 26px; top: 18px;
    color: var(--brand-blue); font-size: 44px;
  }
  .brand-square {
    position: absolute; left: 392px; top: 78px;
    width: 120px; height: 120px; border-radius: 30px;
    background: var(--brand-blue);
  }
  .contact {
    position: absolute; left: 28px; top: 112px;
    color: var(--ink-white);
  }
  .contact-name { font-weight: 700; font-size: 17px; letter-spacing: 0.5px; }
  .contact-role { font-style: italic; font-size: 12px; margin-bottom: 10px; }
  .contact-address { font-style: italic; font-size: 13px; line-height: 1.35; margin-bottom: 8px; }
  .contact-line {
    display: flex; align-items: center; gap: 8px;
    font-style: italic; font-size: 13px; line-height: 1.5;
  }
  .contact-line svg { width: 11px; height: 11px; flex: none; }
</style>
</head>
<body>
<main class="stage">
  <section class="card card-back" aria-label="Card back">
    <span class="wordmark">Tamkor</span>
  </section>

  <section class="card card-front" aria-label="Card front">
    <svg class="front-wave" viewBox="0 0 540 309" preserveAspectRatio="none" aria-hidden="true">
      <path d="M0 64 C140 74 225 128 292 196 C352 258 430 282 540 286 L540 309 L0 309 Z" fill="var(--brand-blue)"/>
      <path d="M0 56 C140 66 230 120 300 190 C360 250 430 274 520 280" fill="none" stroke="var(--brand-deep)" stroke-width="3"/>
    </svg>

    <span class="wordmark">Tamkor</span>
    <div class="brand-square"></div>

    <div class="contact">
      <p class="contact-name">DORIAN PACE</p>
      <p class="contact-role">Owner</p>
      <p class="contact-address">2180 Larkspur Road, Bellmere<br>NC 2, United States</p>
      <p class="contact-line">
        <svg viewBox="0 0 12 12"><path d="M3 1 L5 3.5 L4 5 C4.8 6.6 5.6 7.4 7 8 L8.5 7 L11 9 L9.5 11 C5 10.5 1.5 7 1 2.5 Z" fill="currentColor"/></svg>
        000-000-000-000
      </p>
      <p class="contact-line">
        <svg viewBox="0 0 12 12"><rect x="0.8" y="2.5" width="10.4" height="7" fill="none" stroke="currentColor"/><path d="M0.8 2.5 L6 6.5 L11.2 2.5" fill="none" stroke="currentColor"/></svg>
        info@websitename.com
      </p>
      <p class="contact-line">
        <svg viewBox="0 0 12 12"><circle cx="6" cy="6" r="5" fill="none" stroke="currentColor"/><ellipse cx="6" cy="6" rx="2.2" ry="5" fill="none" stroke="currentColor"/><path d="M1 6 H11" stroke="currentColor"/></svg>
        www.websitename.com
      </p>
    </div>
  </section>
</main>
</body>
</html>
```